Letter Head Design

I need a letter head design based on my company logo that I attached.
Include phone number: (403)582-4316
Address: 347 14th Avenue NE, Calgary, Alberta, Canada, T3K 4R8

Industry/Entity Type

It Company

```html
<!DOCTYPE html>
<html lang="en">
<head>
<meta charset="utf-8">
<title>BrightNest Letterhead</title>
<link href="https://fonts.googleapis.com/css2?family=Arimo:wght@400;700&display=swap" rel="stylesheet">
<style>
  :root {
    --backdrop: #e6e6e6;
    --paper: #ffffff;
    --band-light: #4ba3f2;
    --band-deep: #0a3af2;
    --leaf-green: #6fd42a;
    --brand-blue: #1f66d6;
    --ink: #111111;
    --ghost: #eef3f8;
  }
  * { margin: 0; padding: 0; box-sizing: border-box; }
  html, body { width: 956px; height: 1200px; overflow: hidden; background: var(--backdrop); }
  .canvas { position: relative; width: 956px; height: 1200px; font-family: "Arimo", Arial, sans-serif; }
  .letterhead { position: absolute; left: 53px; top: 62px; width: 847px; height: 1096px; background: var(--paper); overflow: hidden; }
  .top-band { position: absolute; left: 0; top: 0; width: 100%; height: 56px;
    background: linear-gradient(90deg, var(--band-light), var(--band-deep)); }
  .accent-rule { position: absolute; left: 0; top: 62px; width: 100%; height: 5px; background: var(--leaf-green); }
  .brand-tab { position: absolute; left: 67px; top: 14px; width: 142px; height: 110px; background: var(--paper); }
  .brand-square { position: absolute; left: 87px; top: 22px; width: 102px; height: 102px; background: var(--brand-blue); border-radius: 6px; }
  .brand-name { position: absolute; left: 37px; top: 130px; font-size: 32px; font-weight: 700; color: var(--brand-blue); letter-spacing: -0.5px; white-space: nowrap; }
  .contact { position: absolute; left: 615px; top: 110px; border-left: 2px solid var(--leaf-green); padding-left: 13px; color: var(--ink); font-size: 15px; line-height: 19px; }
  .contact-phone { display: flex; align-items: center; gap: 4px; margin-bottom: 9px; }
  .contact-phone svg { width: 15px; height: 15px; }
  .ghost-mark { position: absolute; left: 297px; top: 738px; width: 348px; height: 348px; border: 14px solid var(--ghost); border-radius: 22px; }
</style>
</head>
<body>
<div class="canvas">
  <div class="letterhead">
    <div class="top-band"></div>
    <div class="accent-rule"></div>
    <div class="brand-tab"></div>
    <div class="brand-square"></div>
    <div class="brand-name">BrightNest</div>

    <address class="contact" style="font-style:normal">
      <div class="contact-phone">
        <svg viewBox="0 0 16 16" aria-hidden="true">
          <circle cx="8" cy="8" r="7" fill="none" stroke="#6fd42a" stroke-width="1.4"/>
          <path d="M5.6 4.2 l1.4 0 l0.6 2 l-0.9 0.8 a5 5 0 0 0 2.3 2.3 l0.8 -0.9 l2 0.6 l0 1.4 a1 1 0 0 1 -1 1 a7 7 0 0 1 -6.2 -6.2 a1 1 0 0 1 1 -1 z" fill="#6fd42a"/>
        </svg>
        <span>403-582-4316</span>
      </div>
      <div>347 14th Avenue NE, Calgary</div>
      <div>Alberta, Canada, T3K 4R8</div>
    </address>

    <div class="ghost-mark" aria-hidden="true"></div>
  </div>
</div>
</body>
</html>
```